Veltrano - Mechanic/Collision Center Business Card

We're looking for a business card design for our mechanic/ collision repair shop.

Can be with colours or monochromatic.

See the attached files.

Many thanks

```html
<!DOCTYPE html>
<html lang="pt">
<head>
<meta charset="utf-8">
<title>Veltrano – Business Card</title>
<link href="https://fonts.googleapis.com/css2?family=Montserrat:wght@400;500;700;800&display=swap" rel="stylesheet">
<style>
  :root {
    --page: #d9d9db;
    --card: #171718;
    --blue: #1e9bd7;
    --white: #ffffff;
    --text: #f2f2f2;
  }
  * { margin: 0; padding: 0; box-sizing: border-box; }
  html, body { width: 1200px; height: 1200px; overflow: hidden; }
  body { background: var(--page); font-family: "Montserrat", sans-serif; position: relative; }

  .card { position: absolute; width: 738px; height: 422px; background: var(--card); overflow: hidden; }
  .card--front { left: 230px; top: 109px; }
  .card--back { left: 232px; top: 558px; }

  .brand { position: absolute; display: flex; align-items: center; gap: 12px; }
  .brand__mark { width: 22px; height: 22px; background: var(--blue); }
  .brand__name { color: var(--white); font-weight: 800; letter-spacing: 2px; line-height: 1; }
  .card--front .brand { left: 0; right: 0; top: 178px; justify-content: center; }
  .card--front .brand__name { font-size: 52px; }
  .card--back .brand { left: 371px; width: 335px; top: 290px; justify-content: center; }
  .card--back .brand__name { font-size: 40px; }

  .front-web { position: absolute; left: 0; right: 0; top: 374px; text-align: center; color: var(--text); font-size: 19px; letter-spacing: 0.6px; }

  .accent { position: absolute; background: var(--blue); }
  .accent--left { left: 0; top: 41px; width: 20px; height: 45px; }
  .accent--right { right: 0; top: 37px; width: 18px; height: 45px; }

  .company { position: absolute; left: 29px; top: 38px; }
  .company__name { color: var(--blue); font-weight: 700; font-size: 29px; letter-spacing: 1px; line-height: 1.1; }
  .company__type { color: var(--text); font-size: 18px; margin-top: 1px; }

  .person { position: absolute; right: 26px; top: 34px; text-align: right; }
  .person__name { color: var(--blue); font-size: 26px; letter-spacing: 1px; line-height: 1.1; }
  .person__role { display: inline-block; color: var(--text); font-size: 18px; margin-right: 5px; padding-bottom: 1px; border-bottom: 2px solid var(--blue); }

  .contact-list { position: absolute; list-style: none; color: var(--text); font-size: 19px; letter-spacing: 0.5px; }
  .contact-list li { display: flex; align-items: center; height: 26.5px; gap: 11px; }
  .contact-list svg { width: 18px; height: 18px; fill: var(--blue); flex: none; }
  .contact-list--company { left: 28px; top: 152px; }
  .contact-list--person { right: 28px; top: 128px; }
  .contact-list--person li { justify-content: flex-end; height: 29px; }
  .address { position: absolute; left: 31px; top: 324px; }
  .address svg { width: 16px; height: 24px; }
  .address li { gap: 13px; }
  .icon-square { width: 17px; height: 17px; background: var(--blue); border-radius: 2px; flex: none; }
</style>
</head>
<body>

<section class="card card--front">
  <div class="brand"><span class="brand__mark"></span><span class="brand__name">VELTRANO</span></div>
  <p class="front-web">www.veltrano-auto.pt</p>
</section>

<section class="card card--back">
  <span class="accent accent--left"></span>
  <div class="company">
    <p class="company__name">VELTRANO</p>
    <p class="company__type">LDA</p>
  </div>

  <span class="accent accent--right"></span>
  <div class="person">
    <p class="person__name">RUI MATOS</p>
    <p class="person__role">manager</p>
  </div>

  <ul class="contact-list contact-list--person">
    <li>913580427
      <svg viewBox="0 0 24 24"><path d="M2 9c0-3 5-5 10-5s10 2 10 5v2h-5V9c-1-1-3-1.5-5-1.5S8 8 7 9v2H2z"/><path d="M6 12h12l2 8H4z"/></svg>
    </li>
    <li>+351 913580427
      <svg viewBox="0 0 24 24"><path d="M6.6 10.8a15 15 0 0 0 6.6 6.6l2.2-2.2a1 1 0 0 1 1-.25 11 11 0 0 0 3.6.6 1 1 0 0 1 1 1V20a1 1 0 0 1-1 1A17 17 0 0 1 3 4a1 1 0 0 1 1-1h3.5a1 1 0 0 1 1 1 11 11 0 0 0 .6 3.6 1 1 0 0 1-.25 1z"/></svg>
    </li>
  </ul>

  <ul class="contact-list contact-list--company">
    <li><svg viewBox="0 0 24 24"><path d="M2 9c0-3 5-5 10-5s10 2 10 5v2h-5V9c-1-1-3-1.5-5-1.5S8 8 7 9v2H2z"/><path d="M6 12h12l2 8H4z"/></svg>214470352</li>
    <li><svg viewBox="0 0 24 24"><path d="M6.6 10.8a15 15 0 0 0 6.6 6.6l2.2-2.2a1 1 0 0 1 1-.25 11 11 0 0 0 3.6.6 1 1 0 0 1 1 1V20a1 1 0 0 1-1 1A17 17 0 0 1 3 4a1 1 0 0 1 1-1h3.5a1 1 0 0 1 1 1 11 11 0 0 0 .6 3.6 1 1 0 0 1-.25 1z"/></svg>+351 214470352</li>
    <li><svg viewBox="0 0 24 24"><path d="M2 5h20v14H2z M3 6l9 7 9-7" fill="var(--blue)" stroke="var(--card)" stroke-width="1.5"/></svg>oficina@veltrano-auto.pt</li>
    <li><span class="icon-square"></span>www.veltrano-auto.pt</li>
  </ul>

  <ul class="contact-list address">
    <li><svg viewBox="0 0 16 24"><path d="M8 0a8 8 0 0 1 8 8c0 6-8 16-8 16S0 14 0 8a8 8 0 0 1 8-8zm0 4.5a3.5 3.5 0 1 0 0 7 3.5 3.5 0 0 0 0-7z"/></svg>Rua das Oliveiras, 42</li>
  </ul>

  <div class="brand"><span class="brand__mark"></span><span class="brand__name">VELTRANO</span></div>
</section>

</body>
</html>
```